Medical clinic Flyer for Tovren Medical clinic in Chilliwack, BC

Need a double sided flyer design sized 5.5" x 8.5'' for a medical clinic. The flyer attached for Marlow Crest clinic is a good example of what we are looking for.

We need to focus on advertising this clinic as being a walk in clinic with short wait time. We need to make "walk in clinic Now open" eye catching.

We need to include the following messages:
1. Full Family Practice.
2. Accepting new patients.
3. Walk in clinic open Monday to Friday 9am to 4pm.
4. Short wait times.
5. No appointment needed
6.Check out our state of the art Medical clinic.
7. Velnox, Dermal Fillers, and Corvessa available (Physician Lead)

Target Market(s)

Residents of Chilliwack, BC.

Industry/Entity Type

Healthcare

Requirements
Must have
• Phone number: 18775206348
Addres: 4519 Birchwold Trail Pkwy Unit#312, Chilliwack, BC, V2R 0K7
Nice to have
• Location Map

```html
<!DOCTYPE html>
<html lang="en">
<head>
<meta charset="utf-8">
<title>Tovren Medical Centre – Walk-in Clinic Flyer</title>
<link rel="stylesheet" href="https://fonts.googleapis.com/css2?family=Montserrat:wght@400;500;600;800&family=Raleway:wght@700;800&display=swap">
<style>
  :root {
    --page-bg: #ececec;
    --paper: #ffffff;
    --red: #d71f2b;
    --red-deep: #8e1b22;
    --wine: #6d1519;
    --ink: #131a22;
    --navy: #22304f;
    --navy-light: #2c3d63;
    --photo-warm: #cfc8bd;
    --photo-cool: #b9bcc2;
    --map-fill: #e6ecf2;
  }
  * { margin: 0; padding: 0; box-sizing: border-box; }
  html, body { width: 900px; height: 1200px; overflow: hidden; }
  body {
    background: var(--page-bg);
    position: relative;
    font-family: "Montserrat", Arial, sans-serif;
    color: var(--ink);
  }
  .flyer-side {
    position: absolute;
    left: 79px;
    width: 742px;
    height: 480px;
    overflow: hidden;
    background: var(--paper);
  }
  .flyer-front { top: 80px; }
  .flyer-back { top: 638px; background: var(--navy); }
  .side-art { position: absolute; inset: 0; width: 742px; height: 480px; }
  .abs { position: absolute; }

  /* Front */
  .brand {
    left: 38px; top: 30px;
    display: flex; align-items: center; gap: 10px;
  }
  .brand-dot { width: 34px; height: 34px; border-radius: 50%; background: var(--ink); }
  .brand-name {
    font-weight: 800; font-size: 20px; line-height: 1.05;
    color: var(--red-deep); letter-spacing: 0.5px;
  }
  .headline {
    left: 30px; top: 96px;
    font-family: "Raleway", Arial, sans-serif;
    font-weight: 800; font-size: 46px; line-height: 43px;
    color: var(--red-deep); letter-spacing: -0.5px;
  }
  .headline span { color: var(--red); }
  .hours { left: 30px; top: 198px; font-size: 17px; font-weight: 500; }
  .feature-list {
    left: 30px; top: 246px; list-style: none;
    color: #fff; font-size: 23px; font-weight: 500; letter-spacing: 0.4px;
  }
  .feature-list li { display: flex; align-items: center; gap: 8px; height: 30.5px; }
  .tick { width: 20px; height: 16px; flex: none; }
  .phone-line {
    left: 26px; top: 356px;
    display: flex; align-items: center; gap: 6px;
    font-weight: 800; font-size: 50px; line-height: 50px;
    color: var(--red-deep); letter-spacing: 0.5px;
  }
  .phone-icon { width: 18px; height: 30px; }
  .address {
    left: 30px; top: 421px;
    display: flex; gap: 10px; color: #fff;
    font-size: 16px; font-weight: 500; line-height: 20px; letter-spacing: 0.3px;
  }
  .pin { width: 14px; height: 22px; flex: none; margin-top: 2px; }
  .wait-tag {
    color: #fff; font-family: "Raleway", Arial, sans-serif;
    font-weight: 800; font-size: 35px; line-height: 40px;
  }
  .wait-1 { left: 403px; top: 66px; }
  .wait-2 { left: 476px; top: 112px; }

  /* Back */
  .back-heading {
    right: 27px; top: 28px; text-align: right;
    font-family: "Raleway", Arial, sans-serif;
    font-weight: 800; font-size: 37px; line-height: 43.5px; color: #fff;
  }
  .back-heading span { color: var(--red); }
  .accent-label { right: 30px; color: var(--red); font-size: 18px; font-weight: 500; }
  .available { top: 210px; }
  .physician { top: 353px; }
  .treatments {
    right: 30px; top: 246px; list-style: none; text-align: right;
    color: #fff; font-size: 24px; font-weight: 500;
  }
  .treatments li { display: flex; justify-content: flex-end; align-items: center; gap: 10px; height: 30.5px; }
  .website { right: 30px; top: 434px; color: #fff; font-size: 14px; font-weight: 500; letter-spacing: 0.3px; }
</style>
</head>
<body>

<section class="flyer-side flyer-front">
  <svg class="side-art" viewBox="0 0 742 480">
    <defs>
      <linearGradient id="redPanel" x1="0" y1="0" x2="1" y2="1">
        <stop offset="0" stop-color="#e0222d"/>
        <stop offset="1" stop-color="#7a1519"/>
      </linearGradient>
      <linearGradient id="redBand" x1="0" y1="0" x2="1" y2="0">
        <stop offset="0" stop-color="#d71f2b"/>
        <stop offset="1" stop-color="#7a1519"/>
      </linearGradient>
      <linearGradient id="personTone" x1="0" y1="0" x2="0" y2="1">
        <stop offset="0" stop-color="#f1d7bd"/>
        <stop offset="1" stop-color="#e9eef5"/>
      </linearGradient>
    </defs>
    <rect class="paper-bg" width="742" height="480" fill="#fff"/>
    <path class="red-panel" d="M352 0 H742 V480 H500 C470 380 430 300 400 230 C380 160 362 80 352 0 Z" fill="url(#redPanel)"/>
    <path class="feature-band" d="M0 233 H374 L418 346 H0 Z" fill="#131a22"/>
    <path class="phone-band-edge" d="M374 233 C392 270 405 310 418 346" stroke="#fff" stroke-width="8" fill="none"/>
    <rect class="white-phone-band" x="0" y="346" width="480" height="65" fill="#fff"/>
    <path class="address-band" d="M0 411 H520 C505 440 495 460 488 480 H0 Z" fill="url(#redBand)"/>
    <rect class="doctor-photo" role="img" aria-label="Photo of a smiling doctor in a white coat with a stethoscope, gesturing toward the wait-time message" x="560" y="20" width="182" height="290" rx="60" fill="url(#personTone)" opacity="0.9"/>
    <path class="map-area" role="img" aria-label="Street map showing the clinic location in Chilliwack" d="M430 480 C520 380 620 315 742 290 V480 Z" fill="var(--map-fill)"/>
    <path class="map-swoosh" d="M422 480 C510 372 615 308 742 282" stroke="#131a22" stroke-width="7" fill="none"/>
    <path class="map-swoosh-light" d="M570 340 C630 310 690 295 742 288" stroke="#fff" stroke-width="5" fill="none"/>
    <circle class="stopwatch" role="img" aria-label="Stopwatch illustration" cx="434" cy="138" r="28" fill="#fff" stroke="#e3262f" stroke-width="5"/>
    <circle cx="488" cy="350" r="81" fill="#f2f2f2"/>
    <circle class="storefront-photo" role="img" aria-label="Photo of the clinic storefront" cx="488" cy="350" r="73" fill="#8d8a85"/>
  </svg>

  <div class="abs brand">
    <span class="brand-dot"></span>
    <span class="brand-name">TOVREN<br>MEDICAL CENTRE</span>
  </div>

  <h1 class="abs headline">Walk-in Clinic<br><span>Now Open</span></h1>
  <p class="abs hours">Monday - Friday, 9am to 4pm</p>

  <ul class="abs feature-list">
    <li><svg class="tick" viewBox="0 0 20 16"><path d="M2 8 L8 14 L18 2" stroke="#d71f2b" stroke-width="4" fill="none"/></svg>Full Family Practice</li>
    <li><svg class="tick" viewBox="0 0 20 16"><path d="M2 8 L8 14 L18 2" stroke="#d71f2b" stroke-width="4" fill="none"/></svg>Accepting New Patients</li>
    <li><svg class="tick" viewBox="0 0 20 16"><path d="M2 8 L8 14 L18 2" stroke="#d71f2b" stroke-width="4" fill="none"/></svg>No appointement needed</li>
  </ul>

  <p class="abs phone-line">
    <svg class="phone-icon" viewBox="0 0 18 30"><rect x="2" y="2" width="14" height="26" rx="3" stroke="#131a22" stroke-width="3" fill="none"/></svg>
    18775206348
  </p>

  <p class="abs address">
    <svg class="pin" viewBox="0 0 14 22"><path d="M7 0 C3 0 0 3 0 7 C0 12 7 22 7 22 C7 22 14 12 14 7 C14 3 11 0 7 0 Z" fill="#fff"/><circle cx="7" cy="7" r="3" fill="#d71f2b"/></svg>
    <span>4519 Birchwold Trail Pkwy<br>Unit#312, Chilliwack, BC, V2R 0K7</span>
  </p>

  <p class="abs wait-tag wait-1">Short wait</p>
  <p class="abs wait-tag wait-2">times.</p>
</section>

<section class="flyer-side flyer-back">
  <svg class="side-art" viewBox="0 0 742 480">
    <defs>
      <linearGradient id="navyPanel" x1="0" y1="0" x2="1" y2="1">
        <stop offset="0" stop-color="#1f2a45"/>
        <stop offset="1" stop-color="#2c3d63"/>
      </linearGradient>
      <linearGradient id="roomTone" x1="0" y1="0" x2="1" y2="1">
        <stop offset="0" stop-color="#d8d3c9"/>
        <stop offset="1" stop-color="#a9a7a3"/>
      </linearGradient>
    </defs>
    <rect width="742" height="480" fill="url(#navyPanel)"/>
    <path class="red-swoosh" d="M372 0 H390 C460 150 460 330 380 480 H360 C420 330 420 150 372 0 Z" fill="#b01e26"/>
    <path class="exam-room-photo" role="img" aria-label="Photo of an exam room with examination table, chair, computer and wall-mounted instruments" d="M0 0 H372 C420 150 420 330 380 480 H0 Z" fill="url(#roomTone)"/>
    <path d="M372 0 C420 150 420 330 380 480" stroke="#fff" stroke-width="6" fill="none"/>
    <circle cx="402" cy="341" r="108" fill="#f2f2f2"/>
    <circle class="reception-photo" role="img" aria-label="Photo of the clinic reception and waiting area" cx="402" cy="341" r="100" fill="#b5b4b1"/>
  </svg>

  <h2 class="abs back-heading">Check out our<br>state of the art<br><span>Medical Clinic</span></h2>

  <p class="abs accent-label available">Available</p>
  <ul class="abs treatments">
    <li>Velnox<svg class="tick" viewBox="0 0 20 16"><path d="M2 8 L8 14 L18 2" stroke="#d71f2b" stroke-width="4" fill="none"/></svg></li>
    <li>Dermal Fillers<svg class="tick" viewBox="0 0 20 16"><path d="M2 8 L8 14 L18 2" stroke="#d71f2b" stroke-width="4" fill="none"/></svg></li>
    <li>Corvessa<svg class="tick" viewBox="0 0 20 16"><path d="M2 8 L8 14 L18 2" stroke="#d71f2b" stroke-width="4" fill="none"/></svg></li>
  </ul>
  <p class="abs accent-label physician">Physician Lead</p>
  <p class="abs website">www.tovrenmedcentre.com</p>
</section>

</body>
</html>
```